New Managed IT company needs a business card

We are an IT management and support company that needs a business card design. I have a logo that I'll provide. Blues and blacks match the logo, but i'm open to anything. I want the card to help people take us seriously, but still have some energy and fun in it. The card should communicate stability and a solid company.

Target Market(s)

Target market includes Owners and Presidents at small businesses of 20 - 100 employees in the Pittsburgh PA area.

Industry/Entity Type

Information Technology

Contact Information for Business Card

i am open to other designs, but i imagine having only the logo on one side and then the logo plus all contact details on the other side.

Requirements
Must have
• Our logo
• Company name is optional if the logo makes it obvious
• A name - Lew Tasker
• A title - President
• A phone number - 724-XXX-XXXX
• A mobile phone number - 724-516-0471
• An email address - ltasker@brightlanetech.com
• a website - brightlanetech.com or www.brightlanetech.com
Nice to have
• some people tell me the logo feels like a superhero theme, some fun with that idea might be good. I'm open to ideas.
Should not have
• stock photos of people or computers - especially old looking stuff.

```html
<!DOCTYPE html>
<html lang="en">
<head>
<meta charset="utf-8">
<title>Bright Lane Tech – Business Card</title>
<link rel="stylesheet" href="https://fonts.googleapis.com/css2?family=Open+Sans:wght@400;700&display=swap">
<style>
  :root {
    --page-bg: #eeeff1;
    --card-grey: #6a6b6f;
    --card-grey-light: #727377;
    --accent-blue: #1ea0e6;
    --ink-dark: #1b1c1f;
    --ink-light: #ffffff;
  }
  * { box-sizing: border-box; margin: 0; padding: 0; }
  html, body {
    width: 1200px;
    height: 800px;
    overflow: hidden;
    background: var(--page-bg);
    font-family: "Open Sans", Arial, sans-serif;
  }
  .canvas {
    position: relative;
    width: 1200px;
    height: 800px;
  }
  .card {
    position: absolute;
    top: 250px;
    width: 525px;
    height: 300px;
    background: var(--card-grey);
    overflow: hidden;
    box-shadow: 0 6px 18px rgba(0,0,0,0.18);
  }
  .card--back { left: 50px; }
  .card--front { left: 625px; }

  /* Back side */
  .back-emblem {
    position: absolute;
    left: 110px;
    top: -40px;
    width: 380px;
    height: 380px;
    border-radius: 50%;
    border: 34px solid var(--card-grey-light);
  }
  .brand {
    position: absolute;
    display: flex;
    align-items: center;
    gap: 12px;
  }
  .brand__dot {
    width: 34px;
    height: 34px;
    border-radius: 50%;
    background: var(--accent-blue);
    flex: none;
  }
  .brand__name {
    font-weight: 700;
    font-size: 22px;
    letter-spacing: 2px;
    text-transform: uppercase;
    color: var(--ink-dark);
    line-height: 1.05;
  }
  .card--back .brand {
    left: 50%;
    top: 50%;
    transform: translate(-50%, -50%);
  }

  /* Front side */
  .stripe {
    position: absolute;
    height: 8px;
    background: var(--accent-blue);
  }
  .stripe--top { top: 14px; left: 228px; right: 14px; }
  .stripe--bottom { bottom: 14px; left: 40px; right: 140px; }
  .card--front .brand {
    left: 34px;
    top: 108px;
  }
  .card--front .brand__name { font-size: 19px; }

  .contact {
    position: absolute;
    left: 300px;
    top: 78px;
    color: var(--ink-light);
  }
  .contact__name {
    font-size: 16px;
    font-weight: 400;
    line-height: 1.15;
  }
  .contact__title {
    font-size: 12px;
    color: var(--accent-blue);
    margin-bottom: 14px;
  }
  .contact__list { list-style: none; }
  .contact__item {
    display: flex;
    align-items: center;
    gap: 10px;
    font-size: 12px;
    line-height: 1;
    margin-bottom: 11px;
  }
  .contact__icon {
    width: 14px;
    height: 14px;
    flex: none;
    fill: none;
    stroke: var(--accent-blue);
    stroke-width: 1.6;
  }
  .contact__icon--solid { fill: var(--accent-blue); stroke: none; }
</style>
</head>
<body>
<main class="canvas">

  <section class="card card--back" aria-label="Card back">
    <div class="back-emblem" aria-hidden="true"></div>
    <div class="brand">
      <span class="brand__dot" aria-hidden="true"></span>
      <span class="brand__name">Bright Lane<br>Tech</span>
    </div>
  </section>

  <section class="card card--front" aria-label="Card front">
    <div class="stripe stripe--top"></div>
    <div class="stripe stripe--bottom"></div>

    <div class="brand">
      <span class="brand__dot" aria-hidden="true"></span>
      <span class="brand__name">Bright Lane<br>Tech</span>
    </div>

    <div class="contact">
      <p class="contact__name">Lew Tasker</p>
      <p class="contact__title">President</p>
      <ul class="contact__list">
        <li class="contact__item">
          <svg class="contact__icon contact__icon--solid" viewBox="0 0 16 16" aria-hidden="true"><path d="M3.5 1.5l2.5 0 1 3.5-1.7 1.2a8 8 0 0 0 4.5 4.5L11 9l3.5 1v2.5c0 1-1 2-2 2A11 11 0 0 1 1.5 3.5c0-1 1-2 2-2z"/></svg>
          <span>724 309 2284</span>
        </li>
        <li class="contact__item">
          <svg class="contact__icon" viewBox="0 0 16 16" aria-hidden="true"><rect x="4" y="1" width="8" height="14" rx="1.5"/><line x1="7" y1="12.5" x2="9" y2="12.5"/></svg>
          <span>724 516 0471</span>
        </li>
        <li class="contact__item">
          <svg class="contact__icon" viewBox="0 0 16 16" aria-hidden="true"><path d="M2 6.5a9 9 0 0 1 12 0"/><path d="M4.3 9a5.5 5.5 0 0 1 7.4 0"/><circle class="contact__icon--solid" cx="8" cy="12" r="1.3"/></svg>
          <span>www.brightlanetech.com</span>
        </li>
        <li class="contact__item">
          <svg class="contact__icon contact__icon--solid" viewBox="0 0 16 16" aria-hidden="true"><path d="M1 3.5h14v9H1z"/><path d="M1.5 4l6.5 5 6.5-5" fill="none" stroke="#6a6b6f" stroke-width="1.3"/></svg>
          <span>ltasker@brightlanetech.com</span>
        </li>
      </ul>
    </div>
  </section>

</main>
</body>
</html>
```